Sleep/Snoring Business - Requires Website - Australia

We are seeking a simple to maintain website for our sleep business. The health care business provides diagnostic and treatment solutions for snoring, sleep disorders and other respiratory problems.

Ideally, colours to match the company logo (attached).

The page must be built using WORDPRESS.

Ideally site will have a home page outlining the business, with 5 sub pages - being "Diagnosis" "Treatment Options", "Prodcuts", "About Us", "Contact Us"

The site home page should include a large picture on the home page.

The "Treatment Options" and "Diagnosis" pages must include:
Allow for a few pictures with assocaited text, plus space for some embeded youtube videos.

"Prodcuts" page should have the ability to show 3-4 products across the page with text below.. that can include external URL to products

The "About Us" page must include:
1. a Map (google map) to identify the various locations. There are 6 in total.
2. A Section to describe our doctors/staff - allow for a picture and some text

The "Contact Us" page must include:
email form
telephone details

The overall design should have a clean and medical/safe feeling

Target Market(s)

People who snore and those with sleeping and respiratory disorders

Industry/Entity Type

Health Care

Coding

Coded - Design and coding required

Number of Pages Required

5+ page

Colors

Designer to choose colors to be used in the design.

Requirements
Must have
• The page must be built using WORDPRESS.
• Ideally site will have a home page outlining the business, with 5 sub pages - being "Diagnosis" "Treatment Options", "Prodcuts", "About Us", "Contact Us"
• The site home page should include a large picture on the home page.
• The "Treatment Options" and "Diagnosis" pages must include:
• Allow for a few pictures with assocaited text, plus space for some embeded youtube videos.
• "Prodcuts" page should have the ability to show 3-4 products across the page with text below.. that can include external URL to products
• The "About Us" page must include:
• 1. a Map (google map) to identify the various locations. There are 6 in total.
• 2. A Section to describe our doctors/staff - allow for a picture and some text
• The "Contact Us" page must include:
• email form
• telephone details
• Pictures must be licenced or free to use
Nice to have
• Home page pictures showing people sleeping well, snoring or fresh air (landscape) type transition pictures (at least 3).
Should not have
• Not to look cheap
• This is a high end healthcare business, so must look that way

```html
<!DOCTYPE html>
<html lang="en">
<head>
<meta charset="utf-8">
<title>Restwell Sleep</title>
<link href="https://fonts.googleapis.com/css2?family=Cormorant+Garamond:wght@500;600;700&family=Open+Sans:wght@300;400;600&display=swap" rel="stylesheet">
<style>
:root{
  --navy:#0f3f7a;
  --blue:#adc3e0;
  --blue-mid:#9fb4d9;
  --line:#b9cbe6;
  --text:#333;
  --muted:#555;
  --white:#fff;
}
*{margin:0;padding:0;box-sizing:border-box}
html,body{width:1143px;height:1200px;overflow:hidden;background:var(--white)}
body{font-family:"Open Sans",sans-serif;color:var(--text);position:relative}
.abs{position:absolute}
/* header */
.site-header{position:absolute;left:0;top:0;width:1143px;height:75px;background:var(--white)}
.brand{position:absolute;left:170px;top:12px;width:90px;font-family:"Open Sans",sans-serif;font-weight:600;font-size:18px;line-height:20px;color:var(--navy);letter-spacing:-.3px}
.main-nav{position:absolute;top:44px;left:0;font-size:12px;color:#222}
.main-nav a{position:absolute;white-space:nowrap;text-decoration:none;color:inherit}
.phone-tab{position:absolute;left:850px;top:0;width:150px;height:36px;background:var(--blue);color:var(--white);font-size:12.5px;font-weight:600;display:flex;align-items:center;justify-content:center;gap:7px}
/* hero */
.hero{position:absolute;left:0;top:75px;width:1143px;height:375px;background:linear-gradient(90deg,#e9e6e4 0%,#efe9e5 35%,#f2f3f6 62%,#fafbfd 80%,#fdfdfe 100%)}
.hero-title{position:absolute;left:735px;top:88px;font-family:"Cormorant Garamond",serif;font-weight:500;font-size:56px;color:var(--navy);white-space:nowrap;line-height:1}
.hero-rule{position:absolute;left:737px;top:157px;width:263px;height:1px;background:var(--line)}
.hero-copy{position:absolute;left:744px;top:167px;width:260px;font-size:12.8px;font-weight:300;line-height:21.6px;color:var(--muted)}
.hero-btn{position:absolute;left:815px;top:248px;width:114px;height:43px;background:var(--blue);color:var(--white);font-size:11.5px;font-weight:300;display:flex;align-items:center;justify-content:center}
.dots{position:absolute;top:346px;left:544px;display:flex;gap:6px}
.dots span{width:14px;height:14px;border-radius:50%;background:#aaa}
.dots span:first-child{background:var(--navy)}
/* intro band */
.intro{position:absolute;left:0;top:450px;width:1143px;height:254px;background:var(--blue);text-align:center;color:var(--white)}
.intro-rule{position:absolute;left:142px;width:858px;height:1px;background:#e3ebf6}
.intro h2{position:absolute;left:0;width:100%;top:60px;font-family:"Cormorant Garamond",serif;font-weight:500;font-size:38px;line-height:1}
.intro p{position:absolute;left:155px;width:833px;top:127px;font-size:13.3px;line-height:21.4px;font-weight:400}
/* services */
.service{position:absolute;top:740px;width:253px;height:244px;border:2px solid var(--line);text-align:center}
.service h3{position:absolute;top:-14px;left:50%;transform:translateX(-50%);background:var(--white);padding:0 7px;font-family:"Cormorant Garamond",serif;font-weight:700;font-size:24px;color:var(--blue-mid);letter-spacing:.5px;line-height:1.1;white-space:nowrap}
.service svg{position:absolute;top:30px;left:50%;transform:translateX(-50%)}
.service p{position:absolute;top:94px;left:42px;right:42px;font-size:10.4px;line-height:21.6px;color:#333}
.service .more{position:absolute;top:172px;left:45px;width:161px;height:29px;border:1px solid #333;font-size:10.3px;display:flex;align-items:center;justify-content:center;color:#222}
/* footer */
.site-footer{position:absolute;left:0;top:1006px;width:1143px;height:194px;background:linear-gradient(180deg,#d6e6f8 0%,#e6eff9 50%,#d7e3f1 100%)}
.footer-scene{position:absolute;left:0;top:0;width:1143px;height:194px;background:radial-gradient(ellipse 420px 140px at 700px 210px,rgba(170,190,215,.5),transparent)}
.footer-col h4{font-size:12.5px;font-weight:600;color:#222;margin-bottom:6px}
.footer-col{position:absolute;top:26px;font-size:11.5px;font-weight:300;line-height:21.5px;color:#555;text-align:center}
.about h4{display:inline-block;border-bottom:2px solid #222;padding-bottom:1px;margin-bottom:12px}
.about{text-align:left;left:142px;width:245px}
.about .brand-sm{font-weight:600;font-size:20px;color:var(--navy);margin:2px 0 10px 26px;line-height:1.3}
.about p{font-size:10px;line-height:17px}
.social{display:flex;gap:12px;justify-content:center;margin-top:6px}
.social span{width:16px;height:16px;border-radius:50%;background:var(--blue-mid)}
.copyright{position:absolute;top:172px;left:0;width:100%;text-align:center;font-size:9.8px;font-weight:300;color:#555}
</style>
</head>
<body>
<header class="site-header">
  <div class="brand">Restwell<br>Sleep</div>
  <nav class="main-nav">
    <a style="left:279px">Home</a>
    <a style="left:355px">Diagnosis</a>
    <a style="left:450px">Treatment Options</a>
    <a style="left:597px">Products</a>
    <a style="left:688px">About Us</a>
    <a style="left:781px">Contact Us</a>
  </nav>
  <div class="phone-tab">
    <svg width="14" height="14" viewBox="0 0 24 24" fill="#fff"><path d="M6.6 10.8a15.1 15.1 0 0 0 6.6 6.6l2.2-2.2c.3-.3.7-.4 1-.2 1.1.4 2.3.6 3.6.6.6 0 1 .4 1 1V20c0 .6-.4 1-1 1C10.6 21 3 13.4 3 4c0-.6.4-1 1-1h3.5c.6 0 1 .4 1 1 0 1.3.2 2.5.6 3.6.1.3 0 .7-.2 1z"/></svg>
    +61 2 5550 1742
  </div>
</header>

<section class="hero">
  <div class="abs" role="img" aria-label="Photograph of a woman sleeping peacefully under a white duvet" style="left:0;top:0;width:720px;height:375px;background:linear-gradient(90deg,#e7e2de 0%,#ece3dc 45%,#efe9e5 75%,rgba(242,243,246,0) 100%)"></div>
  <h1 class="hero-title">Sleep Better</h1>
  <div class="hero-rule"></div>
  <p class="hero-copy">Etiam porttitor consectetur lectus, in adipiscing nisi bibendum eu. Lorem ipsum dolor sit amet, consectetur adipiscing elit.</p>
  <div class="hero-btn">FIND OUT HOW</div>
  <div class="dots"><span></span><span></span><span></span></div>
</section>

<section class="intro">
  <div class="intro-rule" style="top:22px"></div>
  <h2>What We Do</h2>
  <p>Suspendisse quam leo, gravida a ullamcorper a, interdum id odio. Ut et ligula ante, nec mollis lacus. Nam nec tellus tortor. Cum sociis natoque penatibus et magnis dis parturient montes, nascetur ridiculus mus. Vestibulum ante ipsum primis in faucibus orci et ultrices posuere cubilia Curae; Class taciti conubia nostra, per himenaeos.</p>
  <div class="intro-rule" style="top:232px"></div>
</section>

<section class="service" style="left:143px">
  <h3>DIAGNOSIS</h3>
  <svg width="40" height="42" viewBox="0 0 40 42" fill="none" stroke="#9fb4d9" stroke-width="3.5" stroke-linecap="round"><path d="M6 3v12a9 9 0 0 0 18 0V3"/><path d="M15 24v6a8 8 0 0 0 16 0v-6"/><circle cx="31" cy="19" r="4.5"/></svg>
  <p>Fusce ullamcorper placerat tortor, placerat consequat diam cursus posuere.</p>
  <div class="more">FIND OUT MORE</div>
</section>

<section class="service" style="left:445px">
  <h3>TREATMENT</h3>
  <svg width="48" height="40" viewBox="0 0 48 40"><rect x="15" y="1.5" width="18" height="8" rx="2" fill="none" stroke="#9fb4d9" stroke-width="3"/><rect x="0" y="8" width="48" height="32" rx="5" fill="#9fb4d9"/><rect x="9" y="8" width="2.5" height="32" fill="#fff"/><rect x="36.5" y="8" width="2.5" height="32" fill="#fff"/><rect x="21" y="15" width="6" height="18" fill="#fff"/><rect x="15" y="21" width="18" height="6" fill="#fff"/></svg>
  <p>Fusce ullamcorper placerat tortor, placerat consequat diam cursus posuere.</p>
  <div class="more">FIND OUT MORE</div>
</section>

<section class="service" style="left:747px">
  <h3>PRODUCTS</h3>
  <svg width="48" height="40" viewBox="0 0 48 40" fill="#9fb4d9"><path d="M0 2h8l2 6h38l-5 18H14l1 4h28v3H12L5 5H0z"/><circle cx="15" cy="37" r="3"/><circle cx="40" cy="37" r="3"/></svg>
  <p>Fusce ullamcorper placerat tortor, placerat consequat diam cursus posuere.</p>
  <div class="more">FIND OUT MORE</div>
</section>

<footer class="site-footer">
  <div class="footer-scene" role="img" aria-label="Faint photograph of a snow-capped mountain range"></div>
  <div class="footer-col about">
    <h4>About Restwell Sleep</h4>
    <div class="brand-sm">Restwell Sleep</div>
    <p>Curabitur at malesuada elit. Nulla mauris sem, hendrerit sed fringilla a, facilisis vitae eros. Nunc eget lacinia felis.</p>
  </div>
  <div class="footer-col" style="left:471px;width:200px">
    <h4>Products</h4>
    Product One<br>Product Two<br>Product Three<br>Product Four
  </div>
  <div class="footer-col" style="left:774px;width:200px">
    <h4>Contact Us</h4>
    18 Harbour Lane,<br>Sydney NSW 2000,<br>Australia
    <div class="social"><span></span><span></span></div>
  </div>
  <div class="copyright">Copyright Restwell Sleep. All rights reserved.</div>
</footer>
</body>
</html>
```